looking for sleek business card to standout from the crowd!

We are a young biotechnology company looking to help you personalize your health through understanding your genetic make up. We need you help in making a clean but sleek business card design using our new logo. The goal? Any time we give our cards out, people say "nice card!" The feel we are going for is "modern-techy". We don't want to come across as an old, giant pharma company, but not trying to be a hipster either.

Target Market(s)

healthcare and biotechnology industry.

Industry/Entity Type

Biotechnology

Contact Information for Business Card

Info to include on the card will be NAME, TITLE, EMAIL, PHONE. The companies website (www.morvalytics.com) should also be on the card some where. Would like the logo, when printed, to be raised.

Requirements
Must have
• The logo we have attached in the color it is in. Fonts for text should lean toward more professional/tech.
Nice to have
• Prefer white/light color background
Should not have
• cartoons, landscape backgrounds images.

```html
<!DOCTYPE html>
<html lang="en">
<head>
<meta charset="utf-8">
<title>Morvalytics Business Card</title>
<link href="https://fonts.googleapis.com/css2?family=Open+Sans:wght@400;600&family=Oswald:wght@600&display=swap" rel="stylesheet">
<style>
  :root {
    --backdrop: #cfcfd2;
    --card-dark: #3d3d3d;
    --logo-tone: #2e2e2e;
    --card-light: #ffffff;
    --name-blue: #1a7bc4;
    --accent-green: #7ac143;
    --text-dark: #333333;
    --divider: #444444;
  }
  * { margin: 0; padding: 0; box-sizing: border-box; }
  html, body {
    width: 1200px; height: 1200px; overflow: hidden;
    background: var(--backdrop);
  }
  .canvas {
    width: 1200px; height: 1200px;
    display: flex; flex-direction: column; align-items: center; justify-content: center;
    gap: 60px;
  }
  .card {
    width: 700px; height: 400px; border-radius: 28px;
    display: flex; align-items: center; justify-content: center;
    box-shadow: 0 4px 14px rgba(0,0,0,0.18);
  }
  .card-front { background: var(--card-dark); }
  .card-back { background: var(--card-light); }

  .logo-lockup { display: flex; align-items: center; gap: 16px; }
  .logo-name {
    font-family: "Open Sans", sans-serif; font-weight: 600;
    font-size: 52px; letter-spacing: 4px; color: var(--logo-tone);
  }
  .logo-dot { width: 46px; height: 46px; border-radius: 50%; background: var(--logo-tone); }

  .identity { display: flex; align-items: center; gap: 20px; }
  .person { text-align: right; }
  .person-name {
    font-family: "Oswald", sans-serif; font-weight: 600;
    font-size: 34px; line-height: 1; color: var(--name-blue); letter-spacing: 0.5px;
  }
  .person-title {
    font-family: "Open Sans", sans-serif; font-size: 17px;
    color: var(--accent-green); margin-top: 4px;
  }
  .divider { width: 2px; height: 82px; background: var(--divider); }
  .contacts { list-style: none; font-family: "Open Sans", sans-serif; font-size: 17px; color: var(--text-dark); }
  .contacts li { display: flex; align-items: center; gap: 10px; line-height: 1.45; }
  .contacts svg { width: 16px; height: 16px; flex: none; }
</style>
</head>
<body>
<main class="canvas">
  <section class="card card-front">
    <div class="logo-lockup">
      <span class="logo-name">MORVALYTICS</span>
      <span class="logo-dot"></span>
    </div>
  </section>

  <section class="card card-back">
    <div class="identity">
      <div class="person">
        <div class="person-name">ADRIAN KELL</div>
        <div class="person-title">Founder/CEO</div>
      </div>
      <div class="divider"></div>
      <ul class="contacts">
        <li>
          <svg viewBox="0 0 16 16" aria-hidden="true"><path fill="#7ac143" d="M3.5 1.5l2.3 2.6-1.3 1.7c.9 2 2.4 3.6 4.4 4.6l1.7-1.3 2.7 2.2-1.2 2.4c-5.4-.6-10-5.2-10.6-10.6z"/></svg>
          000-0000-0000
        </li>
        <li>
          <svg viewBox="0 0 16 16" aria-hidden="true"><rect x="1" y="3.5" width="14" height="9.5" rx="1" fill="#7ac143"/><path d="M1.5 4l6.5 5 6.5-5" fill="none" stroke="#fff" stroke-width="1.3"/></svg>
          info@websitename.com
        </li>
        <li>
          <svg viewBox="0 0 16 16" aria-hidden="true"><g fill="none" stroke="#7ac143" stroke-width="1.3"><circle cx="8" cy="8" r="6.3"/><ellipse cx="8" cy="8" rx="2.8" ry="6.3"/><path d="M1.7 8h12.6M2.8 4.8h10.4M2.8 11.2h10.4"/></g></svg>
          www.websitename.com
        </li>
      </ul>
    </div>
  </section>
</main>
</body>
</html>
```